velturi.org business card design

We need 2-sided business cards for velturi.org; one side will be printed in English (EN), the other in Spanish (ES); the information represnted will be the same.
We are a non-profit that aims to mentor and coach future leaders / visionaries. Our target markets are developing countries (Latin America, Africa, Asia) rather than the developed ("western") world. Our business model works by finding funding to mentor / coach a candidate. We provide several mentors / coaches per candidate which help translate the candidate's vision / dream into a path with objectives and steps.
We want the business cards to transmit our values, which are: innovation, learning / self-improvement, equality (i.e. free from discrimination), boldness, intelligence, thoughtfulness, culture, society, future, sustainability.
We recommend the designers work with these values to produce a bold and innovative design, which does not need to adhere to the traditional criteria for business cards. Please use fresh (modern) colours.

Target Market(s)

Visionaries and thought leaders all over the world, but initially in Latin America. We don't discriminate on age, sex, religion, race or any other difference between people

Industry/Entity Type

Leadership

Contact Information for Business Card

The business cards will contain one language (English / Spanish) per side. It would be nice to have some continuity between the front and the back (e.g. pattern, colours).
Each side will contain the company name, website (www.velturi.org) and a slogan / mantra (which will be provided and can be represented as a placeholder until such time). The other details will be Name, (Function), and contact details (email and phone number).

Font styles to use
Sans Serif

Colors

Designer to choose colors to be used in the design.

Requirements
Must have
• [Side A: ENGLISH --- COMPANY INFO]
• [Company Name] Velturi
• [Slogan / Mantra] Shape your world!
• [Website] velturi.org
• [Side A: ENGLISH --- PERSONAL INFO]
• [Name] Dan Pilcher
• [Job Title] Mentoring Coordinator
• [Phone / WhatsApp] +51 947 218 306
• [eMail] dan@velturi.org
• [Side B: SPANISH --- COMPANY INFO]
• [Company Name] Velturi
• [Slogan / Mantra] ¡Moldea tu mundo!
• [Website] velturi.org
• [Side B: SPANISH --- PERSONAL INFO]
• [Name] Daniel Pilcher
• [Job Title] Coordinador de Mentoreo
• [eMail] dan@velturi.org
• [SIDE A: ENGLISH --- Central Values]
• - Future
• - Growth
• - Leadership
• [SIDE B: SPANISH --- Central Values]
• - Futuro
• - Liderazgo
• - Crecimiento
Nice to have
• Innovative and different design. Modern and fresh. Bold and clever.
• Secondary Values (we would like represented) are:
• [SIDE A: ENGLISH --- Secondary Values]
• - Equality
• - Innovation
• - Sustainability
• [SIDE B: SPANISH --- Secondary Values]
• - Igualdad
• - Innovación
• - Sostenibilidad
Should not have
• Please note that the images I have attached to this brief are just some images that I liked while browsing for material for the website. It does not imply I want these colours or this type of design, just that I felt these images had a good feel.

```html
<!DOCTYPE html>
<html lang="en">
<head>
<meta charset="utf-8">
<title>Velturi – business cards</title>
<link rel="stylesheet" href="https://fonts.googleapis.com/css2?family=Montserrat:wght@800;900&family=Nunito+Sans:wght@300;400&display=swap">
<style>
  :root {
    --green: #4fa98a;
    --coral: #d9674c;
    --white: #ffffff;
    --heavy: "Montserrat", sans-serif;
    --light: "Nunito Sans", sans-serif;
  }
  html, body {
    margin: 0;
    padding: 0;
    width: 1117px;
    height: 1200px;
    overflow: hidden;
    background: var(--white);
  }
  .canvas {
    position: relative;
    width: 1117px;
    height: 1200px;
    overflow: hidden;
  }
  .card {
    position: absolute;
    width: 965px;
    height: 545px;
    color: var(--white);
    transform-origin: 0 0;
  }
  .card--en { left: 11px; top: 0; --band: var(--green); --body: var(--coral); }
  .card--es { left: 2px; top: 636px; transform: scale(1.049); --band: var(--coral); --body: var(--green); }

  .card__band {
    position: absolute;
    left: 0; top: 0;
    width: 100%;
    height: 122px;
    background: var(--band);
  }
  .card__body {
    position: absolute;
    left: 0; top: 122px;
    width: 100%;
    height: 423px;
    background: var(--body);
  }
  .brand {
    position: absolute;
    left: 0; top: 0;
    width: 459px;
    height: 122px;
    display: flex;
    align-items: center;
    justify-content: center;
    font-family: var(--heavy);
    font-weight: 900;
    font-size: 40px;
    letter-spacing: 5px;
  }
  .band__divider {
    position: absolute;
    left: 459px; top: 30px;
    width: 2px; height: 76px;
    background: var(--body);
  }
  .slogan {
    position: absolute;
    left: 461px; top: 0;
    width: 504px;
    height: 122px;
    display: flex;
    align-items: center;
    justify-content: center;
    font-family: var(--light);
    font-weight: 400;
    font-size: 31px;
    letter-spacing: 3.5px;
  }
  .person {
    position: absolute;
    left: 34px; top: 210px;
    width: 460px;
  }
  .person__name {
    margin: 0;
    font-family: var(--heavy);
    font-weight: 900;
    font-size: 36px;
    letter-spacing: 3px;
    line-height: 1.1;
    white-space: nowrap;
  }
  .person__role {
    margin: 8px 0 0;
    font-family: var(--light);
    font-weight: 300;
    font-size: 24px;
    letter-spacing: 2.5px;
    white-space: nowrap;
  }
  .contacts {
    position: absolute;
    left: 504px; top: 156px;
    margin: 0; padding: 0;
    list-style: none;
  }
  .contact {
    display: flex;
    align-items: center;
    height: 56px;
    margin-bottom: 15px;
    font-family: var(--light);
    font-weight: 400;
    font-size: 32px;
    white-space: nowrap;
  }
  .contact__icon {
    width: 55px; height: 55px;
    border-radius: 50%;
    background: var(--white);
    display: flex;
    align-items: center;
    justify-content: center;
    margin-right: 10px;
    color: var(--body);
    flex: none;
  }
  .contact__icon--web {
    font-family: var(--light);
    font-size: 15px;
    color: var(--band);
    position: relative;
  }
  .contact__cursor {
    position: absolute;
    left: 32px; top: 34px;
  }
  .values {
    position: absolute;
    left: 0; top: 377px;
    width: 100%;
  }
  .value {
    position: absolute;
    top: 0;
    width: 200px;
    text-align: center;
  }
  .value--future     { left: 20px; }
  .value--leadership { left: 349px; }
  .value--growth     { left: 702px; }
  .value__icon {
    width: 110px; height: 110px;
    margin: 0 auto;
    border-radius: 50%;
    background: var(--white);
    display: flex;
    align-items: center;
    justify-content: center;
    color: var(--band);
  }
  .value__label {
    display: block;
    margin-top: 6px;
    font-family: var(--heavy);
    font-weight: 900;
    font-size: 21px;
    letter-spacing: 2.5px;
  }
  .value--leadership .value__label { margin-top: 10px; }
</style>
</head>
<body>
<main class="canvas">

  <section class="card card--en" lang="en">
    <div class="card__band"></div>
    <div class="card__body"></div>
    <div class="brand">VELTURI</div>
    <div class="band__divider"></div>
    <div class="slogan">Shape your world!</div>

    <div class="person">
      <h2 class="person__name">DAN PILCHER</h2>
      <p class="person__role">mentoring coordinator</p>
    </div>

    <ul class="contacts">
      <li class="contact">
        <span class="contact__icon contact__icon--web">www
          <svg class="contact__cursor" width="12" height="12" viewBox="0 0 12 12"><path d="M10 10 L3 3 M3 3 h4 M3 3 v4" stroke="currentColor" stroke-width="1.6" fill="none"/></svg>
        </span>velturi.org</li>
      <li class="contact">
        <span class="contact__icon">
          <svg width="30" height="22" viewBox="0 0 30 22"><rect x="0" y="0" width="30" height="22" rx="2" fill="currentColor"/><path d="M1 2 L15 12 L29 2" stroke="#fff" stroke-width="2.2" fill="none"/></svg>
        </span>dan@velturi.org</li>
      <li class="contact">
        <span class="contact__icon">
          <svg width="28" height="28" viewBox="0 0 24 24"><path fill="currentColor" d="M6.6 10.8a15 15 0 0 0 6.6 6.6l2.2-2.2a1 1 0 0 1 1-.25 11.4 11.4 0 0 0 3.6.57 1 1 0 0 1 1 1V20a1 1 0 0 1-1 1A17 17 0 0 1 3 4a1 1 0 0 1 1-1h3.5a1 1 0 0 1 1 1c0 1.25.2 2.45.57 3.57a1 1 0 0 1-.25 1z"/></svg>
        </span>+51 947 218 306</li>
    </ul>

    <div class="values">
      <div class="value value--future">
        <div class="value__icon">
          <svg width="64" height="56" viewBox="0 0 64 56" fill="none" stroke="currentColor" stroke-width="3.5" stroke-linecap="round"><path d="M40 10 A22 22 0 1 0 30 50"/><path d="M26 14 V30 L16 38"/><path d="M36 4 L42 10 L35 15"/><path d="M36 40 c3-5 8-5 10 0 s7 5 10 0 s-7-5-10 0 s-7 5-10 0z"/></svg>
        </div>
        <span class="value__label">future</span>
      </div>
      <div class="value value--leadership">
        <div class="value__icon">
          <svg width="54" height="50" viewBox="0 0 54 50" fill="none" stroke="currentColor" stroke-width="3.5" stroke-linecap="round" stroke-linejoin="round"><path d="M3 2 V47 H51"/><path d="M10 38 L21 24 L30 32 L46 12"/><path d="M38 12 H46 V20"/></svg>
        </div>
        <span class="value__label">leadership</span>
      </div>
      <div class="value value--growth">
        <div class="value__icon">
          <svg width="56" height="56" viewBox="0 0 56 56" fill="none" stroke="currentColor" stroke-width="3"><circle cx="28" cy="6" r="4"/><path d="M22 16 a6 6 0 0 1 12 0"/><path d="M28 18 V28 M8 28 H48 M8 28 V36 M28 28 V36 M48 28 V36"/><circle cx="8" cy="41" r="4"/><circle cx="28" cy="41" r="4"/><circle cx="48" cy="41" r="4"/><path d="M2 52 a6 6 0 0 1 12 0 M22 52 a6 6 0 0 1 12 0 M42 52 a6 6 0 0 1 12 0"/></svg>
        </div>
        <span class="value__label">growth</span>
      </div>
    </div>
  </section>

  <section class="card card--es" lang="es">
    <div class="card__band"></div>
    <div class="card__body"></div>
    <div class="brand">VELTURI</div>
    <div class="band__divider"></div>
    <div class="slogan">¡Moldea tu mundo!</div>

    <div class="person">
      <h2 class="person__name">DANIEL PILCHER</h2>
      <p class="person__role">coordinador de mentoreo</p>
    </div>

    <ul class="contacts">
      <li class="contact">
        <span class="contact__icon contact__icon--web">www
          <svg class="contact__cursor" width="12" height="12" viewBox="0 0 12 12"><path d="M10 10 L3 3 M3 3 h4 M3 3 v4" stroke="currentColor" stroke-width="1.6" fill="none"/></svg>
        </span>velturi.org</li>
      <li class="contact">
        <span class="contact__icon">
          <svg width="30" height="22" viewBox="0 0 30 22"><rect x="0" y="0" width="30" height="22" rx="2" fill="currentColor"/><path d="M1 2 L15 12 L29 2" stroke="#fff" stroke-width="2.2" fill="none"/></svg>
        </span>dan@velturi.org</li>
      <li class="contact">
        <span class="contact__icon">
          <svg width="28" height="28" viewBox="0 0 24 24"><path fill="currentColor" d="M6.6 10.8a15 15 0 0 0 6.6 6.6l2.2-2.2a1 1 0 0 1 1-.25 11.4 11.4 0 0 0 3.6.57 1 1 0 0 1 1 1V20a1 1 0 0 1-1 1A17 17 0 0 1 3 4a1 1 0 0 1 1-1h3.5a1 1 0 0 1 1 1c0 1.25.2 2.45.57 3.57a1 1 0 0 1-.25 1z"/></svg>
        </span>+51 947 218 306</li>
    </ul>

    <div class="values">
      <div class="value value--future">
        <div class="value__icon">
          <svg width="64" height="56" viewBox="0 0 64 56" fill="none" stroke="currentColor" stroke-width="3.5" stroke-linecap="round"><path d="M40 10 A22 22 0 1 0 30 50"/><path d="M26 14 V30 L16 38"/><path d="M36 4 L42 10 L35 15"/><path d="M36 40 c3-5 8-5 10 0 s7 5 10 0 s-7-5-10 0 s-7 5-10 0z"/></svg>
        </div>
        <span class="value__label">futuro</span>
      </div>
      <div class="value value--leadership">
        <div class="value__icon">
          <svg width="54" height="50" viewBox="0 0 54 50" fill="none" stroke="currentColor" stroke-width="3.5" stroke-linecap="round" stroke-linejoin="round"><path d="M3 2 V47 H51"/><path d="M10 38 L21 24 L30 32 L46 12"/><path d="M38 12 H46 V20"/></svg>
        </div>
        <span class="value__label">liderazgo</span>
      </div>
      <div class="value value--growth">
        <div class="value__icon">
          <svg width="56" height="56" viewBox="0 0 56 56" fill="none" stroke="currentColor" stroke-width="3"><circle cx="28" cy="6" r="4"/><path d="M22 16 a6 6 0 0 1 12 0"/><path d="M28 18 V28 M8 28 H48 M8 28 V36 M28 28 V36 M48 28 V36"/><circle cx="8" cy="41" r="4"/><circle cx="28" cy="41" r="4"/><circle cx="48" cy="41" r="4"/><path d="M2 52 a6 6 0 0 1 12 0 M22 52 a6 6 0 0 1 12 0 M42 52 a6 6 0 0 1 12 0"/></svg>
        </div>
        <span class="value__label">crecimiento</span>
      </div>
    </div>
  </section>

</main>
</body>
</html>
```